An effective double sided Marketing Postcard Design with a compelling call to action

I want to design an oversized postcard that can be mailed without an envelope. I want a postcard that that inspires and also informs people of when to cal me "If this is happening...call me" I am attaching this file but know I am open to any other ideas. Enclosed is one image, logo and picture and services if they fit anywhere. I like the picture of the one girl with gloves or will be open to using both the boy and the girl.I enclosed the text to go on the front and the back of the card in a word doc, not sure how many will fit on the back of the card. I'd like it to appear like these do: http://www.dailyvelmorpress.com/2014/12/19/super-hero-inspirational-quotes_n_6272328.html

Target Market(s)

Executives, Technology leaders, CIO's, CMO's, Managers

Industry/Entity Type

Information Technology

Font styles to use
Serif

Colors
33a6d7
f04a50

Requirements
Must have
• A fun graphic image or cartoon that makes the person laugh or smile. A great layout of the "When " " is happening Call me!" I'd like to have it be something they will keep in their desk for reference or they will immediately call.
• Use my brand colors which are attached. Use the font similar to the brand color guide for headlines.
Nice to have
• An oversized card designed.
Should not have
• typos or misaligned sentences

```html
<!DOCTYPE html>
<html lang="en">
<head>
<meta charset="utf-8">
<title>Bold Compass – Postcard</title>
<link rel="stylesheet" href="https://fonts.googleapis.com/css2?family=Playfair+Display:wght@400;700&family=Lora:wght@400;500&display=swap">
<style>
  :root {
    --brand-blue: #33a6d7;
    --brand-red: #f04a50;
    --deep-red: #c9333a;
    --ink: #2f2f33;
    --paper: #ffffff;
    --stage: #e4e6e9;
    --sky-top: #8fbfe0;
    --sky-mid: #d7e8f3;
    --sky-low: #f3f7fa;
    --rule: #b9c3cc;
  }
  * { box-sizing: border-box; margin: 0; padding: 0; }
  html, body { width: 900px; height: 1200px; overflow: hidden; }
  body { background: var(--stage); font-family: "Lora", serif; color: var(--ink); position: relative; }

  .postcard {
    position: absolute; left: 60px; width: 780px; height: 520px;
    background: var(--paper); overflow: hidden;
    box-shadow: 0 6px 18px rgba(0,0,0,.18);
  }
  .postcard--front { top: 50px; }
  .postcard--back  { top: 630px; }

  /* FRONT */
  .hero-photo {
    position: absolute; inset: 0;
    background:
      radial-gradient(ellipse 32% 55% at 76% 55%, rgba(196,40,48,.55), rgba(196,40,48,0) 70%),
      radial-gradient(ellipse 18% 22% at 80% 22%, rgba(150,110,70,.45), rgba(150,110,70,0) 70%),
      linear-gradient(180deg, var(--sky-top) 0%, var(--sky-mid) 45%, var(--sky-low) 100%);
  }
  .brand {
    position: absolute; left: 28px; top: 30px;
    display: flex; align-items: center; gap: 10px;
  }
  .brand__dot { width: 18px; height: 18px; border-radius: 50%; background: var(--brand-red); }
  .brand__name {
    font-family: "Playfair Display", serif; font-weight: 400;
    color: var(--deep-red); font-size: 28px; line-height: 1;
  }
  .front-message {
    position: absolute; left: 28px; top: 318px; width: 470px;
  }
  .front-message__headline {
    font-family: "Playfair Display", serif; font-weight: 400;
    color: var(--brand-red); font-size: 24px; line-height: 1.25;
  }
  .front-message__lead {
    font-family: "Playfair Display", serif; font-size: 22px; line-height: 1.3;
    color: var(--deep-red); margin-top: 4px;
  }
  .front-message__lead b { font-weight: 700; }
  .front-band {
    position: absolute; left: 0; right: 0; bottom: 0; height: 22px; background: var(--brand-blue);
  }

  /* BACK */
  .back-band { position: absolute; left: 0; right: 0; top: 0; height: 14px; background: var(--brand-blue); }
  .divider { position: absolute; left: 0; top: 0; }
  .when {
    position: absolute; left: 30px; top: 34px; width: 400px;
  }
  .when__title {
    font-family: "Playfair Display", serif; font-weight: 700;
    color: var(--deep-red); font-size: 44px; line-height: 1;
  }
  .when__list {
    list-style: none; margin-top: 14px;
    font-size: 10.6px; line-height: 1.42; color: var(--brand-red);
  }
  .hero-kid {
    position: absolute; left: 36px; bottom: 22px; width: 70px; height: 100px;
    background: linear-gradient(180deg, #7fb4d8 0%, #c33b3f 60%, #a9c8dc 100%);
    border-radius: 4px;
  }
  .stamp {
    position: absolute; right: 34px; top: 36px; width: 86px; height: 100px;
    border: 1.5px dashed var(--rule);
  }
  .address { position: absolute; right: 34px; top: 200px; width: 250px; }
  .address__line { height: 1px; background: var(--rule); margin-bottom: 30px; }
  .back-mark {
    position: absolute; right: 40px; bottom: 34px; display: flex; align-items: center; gap: 8px;
  }
  .back-mark__dot { width: 14px; height: 14px; border-radius: 50%; background: var(--brand-blue); }
  .back-mark__name {
    font-family: "Playfair Display", serif; font-size: 17px; color: var(--brand-red);
  }
</style>
</head>
<body>

<section class="postcard postcard--front">
  <div class="hero-photo" role="img" aria-label="Photo of a young girl in a red cape, blue mask and red boxing gloves punching forward against a bright sky"></div>
  <header class="brand">
    <span class="brand__dot"></span>
    <span class="brand__name">Bold Compass</span>
  </header>
  <div class="front-message">
    <h1 class="front-message__headline">Activate your Inner Bold Leader!</h1>
    <p class="front-message__lead">When you want <b>super hero</b> results, you find friends in unexpected places.</p>
  </div>
  <div class="front-band"></div>
</section>

<section class="postcard postcard--back">
  <div class="back-band"></div>
  <svg class="divider" width="780" height="520" viewBox="0 0 780 520" aria-hidden="true">
    <path d="M400 14 C 470 140, 470 360, 395 520" fill="none" stroke="var(--brand-red)" stroke-width="2.5"/>
  </svg>
  <div class="when">
    <h2 class="when__title">When</h2>
    <ul class="when__list">
      <li>it is taking twice as long to get things done due to turf wars</li>
      <li>you are tired of key initiatives not being followed</li>
      <li>you are asked to play an unwinnable game</li>
      <li>you are frustrated with a dominant person causing delays</li>
      <li>you need your team to play full out in a high stakes game</li>
      <li>you find your people “sheepwalking” instead of taking a lead</li>
      <li>you don’t want to pay for the same work twice by doing costly rework</li>
      <li>you don’t have the time to be creative</li>
      <li>you are exhausted by a calendar overbooked with meetings</li>
      <li>you need to move visibly within the organization</li>
      <li>you want to navigate internal and external politics with ease</li>
      <li>you want to be seen as a valued member of the organization</li>
      <li>you want to lead with influence, impact and ingenuity using your unique super powers!</li>
    </ul>
  </div>
  <div class="hero-kid" role="img" aria-label="Small photo of a boy in a red cape and mask standing with arm raised"></div>
  <div class="stamp"></div>
  <div class="address">
    <div class="address__line"></div>
    <div class="address__line"></div>
    <div class="address__line"></div>
    <div class="address__line"></div>
  </div>
  <div class="back-mark">
    <span class="back-mark__dot"></span>
    <span class="back-mark__name">Bold Compass</span>
  </div>
</section>

</body>
</html>
```